Medical Device Company needs website

We are a start-up medical device company looking to sell boot (foot) and brace (ankle) products on Shopify. We are still working on the name but you can use Kaltir as a placeholder- no logo yet)

Website information:
- Look: modern/tech with clean lines and symmetry.
- Colors: teal, white, black, and greys.
- Headers: home, shop, about us, help, blog
- Icons (upper right): search, my account and shopping cart
-place to sign up for newsletter

```html
<!DOCTYPE html>
<html lang="en">
<head>
<meta charset="utf-8">
<title>Kaltir — Orthopedic Boots & Braces</title>
<link href="https://fonts.googleapis.com/css2?family=Poppins:wght@400;500;600;700&display=swap" rel="stylesheet">
<style>
:root{
  --teal:#0b8a84;
  --teal-dark:#087570;
  --mint:#d7ecea;
  --mint-soft:#e9f4f3;
  --ink:#111111;
  --grey-text:#6b6b6b;
  --grey-light:#e9e9e9;
  --line:#ececec;
  --white:#ffffff;
  --star:#f5b622;
}
*{box-sizing:border-box;margin:0;padding:0}
html,body{width:1200px;height:3924px;overflow:hidden}
body{position:relative;font-family:'Poppins',sans-serif;color:var(--ink);background:var(--white)}
.abs{position:absolute}
svg{display:block}

/* top bar + nav */
.promo-bar{top:0;left:0;width:1200px;height:30px;background:var(--teal);color:#fff;font-size:10px;display:flex;align-items:center;justify-content:center;gap:6px}
.nav{top:30px;left:0;width:1200px;height:64px}
.logo{font-weight:700;font-size:25px;color:#555}
.nav .logo{left:107px;top:16px}
.nav-links{left:430px;top:24px;display:flex;gap:0;font-size:12px}
.nav-links a{color:var(--ink);text-decoration:none;width:0;white-space:nowrap}
.nav-links a.active{color:var(--teal)}
.nav-icons{left:992px;top:20px;display:flex;gap:10px}
.icon-btn{width:26px;height:26px;border:1px solid #cfcfcf;border-radius:50%;display:flex;align-items:center;justify-content:center}

/* hero */
.side-card{top:96px;width:68px;height:406px;background:var(--grey-light);border-radius:16px}
.hero{top:96px;left:107px;width:986px;height:406px;background:var(--teal);border-radius:16px;overflow:hidden}
.hero h1{left:99px;top:126px;font-size:35px;font-weight:700;line-height:47px;color:#fff}
.btn{display:inline-flex;align-items:center;justify-content:center;border-radius:20px;font-size:11px;font-weight:500;text-decoration:none}
.btn-white{background:#fff;color:var(--ink)}
.btn-teal{background:var(--teal);color:#fff}
.hero .btn{left:99px;top:245px;width:94px;height:31px}
.photo{display:block}
.hero-photo{left:525px;top:30px;width:240px;height:376px;background:linear-gradient(180deg,#eef0f3 0%,#d8dce2 55%,#c9a57a 78%,#f2f2f2 100%);border-radius:60px 60px 10px 10px;opacity:.9}
.slides{left:930px;top:76px;width:30px;color:#fff;text-align:center}
.slides .bar{width:1px;height:32px;background:#fff;margin:0 auto}
.slides .cur{font-size:22px;margin-top:50px}
.slides .n{font-size:11px;margin-top:20px}

/* headings */
.h2{font-size:32px;font-weight:600;width:1200px;text-align:center;left:0}

/* categories */
.cat{top:634px;width:422px;height:245px;border-radius:14px;overflow:hidden}
.cat-a{left:163px;background:#ececec}
.cat-b{left:603px;background:var(--mint-soft)}
.cat h3{position:absolute;left:25px;top:80px;font-size:19px;font-weight:600}
.cat .btn{position:absolute;left:25px;top:131px;width:96px;height:31px}
.cat-blob{position:absolute;left:200px;top:60px;width:260px;height:260px;border-radius:50%;background:#fff;opacity:.8}
.cat-photo{position:absolute;left:215px;top:20px;width:150px;height:215px;border-radius:20px}

/* bestseller */
.best-title{left:163px;top:952px;font-size:31px;font-weight:600}
.arrow-btn{width:34px;height:34px;border-radius:50%;display:flex;align-items:center;justify-content:center}
.prod{top:1017px;width:201px;height:290px;background:#fff;border-radius:10px;box-shadow:0 3px 14px rgba(0,0,0,.06)}
.prod-img{position:absolute;left:6px;top:6px;width:189px;height:183px;border-radius:8px;background:var(--mint-soft)}
.prod-img .ph{position:absolute;left:55px;top:20px;width:80px;height:145px;border-radius:14px}
.heart{position:absolute;right:12px;top:14px}
.prod h4{position:absolute;left:18px;top:207px;font-size:12px;font-weight:600}
.price{position:absolute;left:18px;top:240px;font-size:12.5px;font-weight:600;color:var(--teal)}
.price s{color:#888;font-weight:400;font-size:11px;margin-left:10px}
.prod .go{position:absolute;left:28px;top:278px;width:30px;height:30px;border-radius:50%;background:var(--teal);display:flex;align-items:center;justify-content:center}

/* about */
.about{top:1398px;left:0;width:1200px;height:539px;background:var(--mint)}
.about-pill1{left:107px;top:52px;width:237px;height:332px;border-radius:119px;background:#b9dcd9}
.about-pill2{left:364px;top:114px;width:206px;height:376px;border-radius:103px;background:linear-gradient(180deg,#cfd1d3,#bfc2c5)}
.about h2{left:643px;top:178px;font-size:31px;font-weight:600}
.about p{left:643px;width:382px;font-size:11.2px;line-height:19px;color:#555}
.about .btn{left:643px;top:412px;width:100px;height:33px}

/* why */
.why{top:2070px;width:279px;height:125px;border:1px solid var(--line);border-radius:10px;background:#fff}
.why .ico{position:absolute;left:18px;top:30px;width:62px;height:62px;border-radius:50%;background:var(--teal);display:flex;align-items:center;justify-content:center}
.why h4{position:absolute;left:97px;top:34px;font-size:14.5px;font-weight:600}
.why p{position:absolute;left:97px;top:64px;width:170px;font-size:10.5px;line-height:18px;color:#666}

/* reviews */
.reviews{top:2269px;left:0;width:1200px;height:584px;background:var(--mint)}
.reviews h2{left:162px;top:64px;font-size:31px;font-weight:600}
.rating-sum{left:836px;top:76px;display:flex;align-items:center;gap:12px;font-size:13.5px;font-weight:600}
.filter{left:1043px;top:60px;width:50px;height:46px;border-radius:8px;background:#fff;display:flex;align-items:center;justify-content:center}
.rev-row{left:0;width:1200px;height:190px;-webkit-mask-image:linear-gradient(90deg,transparent 40px,#000 250px,#000 950px,transparent 1160px);mask-image:linear-gradient(90deg,transparent 40px,#000 250px,#000 950px,transparent 1160px)}
.rev{position:absolute;top:0;width:288px;height:185px;background:#fff;border-radius:8px;padding:14px 16px}
.stars{color:var(--star);font-size:14px;letter-spacing:1px}
.rev .date{font-size:10px;color:#777;margin-top:4px}
.rev .who{display:flex;align-items:center;gap:8px;margin-top:6px;font-size:14px;font-weight:600}
.rev .who span{font-size:10px;font-weight:400;color:#888;display:flex;align-items:center;gap:4px}
.rev p{font-size:10px;line-height:17px;color:#555;margin-top:12px}
.rev .item{display:flex;align-items:center;gap:10px;margin-top:10px;font-size:10px;color:#777}
.thumb{width:32px;height:32px;border:1px solid #ddd;border-radius:6px;background:#f2f2f2}

/* blog */
.post{top:2987px;width:273px;height:361px;background:#fff;border-radius:8px;box-shadow:0 3px 14px rgba(0,0,0,.06);overflow:hidden}
.post-img{position:absolute;left:0;top:0;width:273px;height:177px}
.post .date{position:absolute;left:18px;top:197px;font-size:10.5px;font-weight:500;display:flex;gap:10px;align-items:center}
.post .rule{position:absolute;left:18px;top:221px;width:237px;height:1px;background:var(--line)}
.post h4{position:absolute;left:18px;top:245px;font-size:12.5px;font-weight:600}
.post p{position:absolute;left:18px;top:277px;width:220px;font-size:10.5px;line-height:17px;color:#666}
.post .more{position:absolute;left:18px;top:325px;font-size:11.5px;font-weight:500;color:var(--teal);display:flex;gap:8px;align-items:center}

/* newsletter + footer */
.footer{top:3578px;left:0;width:1200px;height:346px;background:#000}
.newsletter{top:3424px;left:163px;width:862px;height:227px;border-radius:18px;background:var(--teal);overflow:hidden}
.newsletter h2{left:44px;top:56px;font-size:31px;font-weight:700;color:#fff}
.newsletter p{left:44px;top:109px;font-size:12.5px;color:#eaf6f5}
.nl-form{left:44px;top:150px;width:380px;height:36px;background:#fff;border-radius:18px}
.nl-form span{position:absolute;left:18px;top:11px;font-size:10px;color:#888}
.nl-form .sub{position:absolute;right:0;top:0;width:118px;height:36px;border-radius:18px;background:#000;color:#fff;font-size:12px;display:flex;align-items:center;justify-content:center}
.nl-photo{left:600px;top:0;width:160px;height:227px;background:linear-gradient(180deg,#1b1b1b,#2a2a2a 70%,#c89a7e);border-radius:0 0 60px 60px}
.f-logo{left:163px;top:3700px;font-size:25px;font-weight:700;color:#fff}
.f-col{top:3704px;color:#fff}
.f-col h5{font-size:13px;font-weight:500;margin-bottom:22px}
.f-col li{list-style:none;font-size:10.5px;line-height:23px;color:#ddd}
.contact{display:flex;align-items:center;gap:12px;font-size:13px;font-weight:600;margin-bottom:14px}
.contact .c{width:30px;height:30px;border-radius:50%;background:var(--teal);display:flex;align-items:center;justify-content:center}
.follow{left:163px;top:3863px;width:137px;height:36px;border-radius:18px;background:#5a31f4;color:#fff;font-size:11.5px;font-weight:500;display:flex;align-items:center;justify-content:center;gap:6px}
.cards{left:415px;top:3873px;display:flex;gap:13px}
.cards i{display:block;width:24px;height:16px;border-radius:3px;background:#fff}
.copy{left:950px;top:3876px;font-size:10px;color:#ccc}
</style>
</head>
<body>

<div class="abs promo-bar">
  <svg width="10" height="10" viewBox="0 0 10 10"><path d="M1 5l3 3 5-7" fill="none" stroke="#fff" stroke-width="1.5"/></svg>
  Football Sale Save Up To 30% Off On Sports Braces
</div>

<header class="abs nav">
  <div class="abs logo">Kaltir</div>
  <nav class="abs nav-links">
    <a class="active" style="margin-right:77px">Home</a>
    <a style="margin-right:72px">Shop</a>
    <a style="margin-right:95px">About Us</a>
    <a style="margin-right:69px">Help</a>
    <a>Blog</a>
  </nav>
  <div class="abs nav-icons">
    <div class="icon-btn"><svg width="12" height="12" viewBox="0 0 12 12"><circle cx="5" cy="5" r="3.8" fill="none" stroke="#0b8a84" stroke-width="1.4"/><path d="M8 8l3 3" stroke="#0b8a84" stroke-width="1.4"/></svg></div>
    <div class="icon-btn"><svg width="12" height="12" viewBox="0 0 12 12"><circle cx="6" cy="4" r="2.6" fill="none" stroke="#0b8a84" stroke-width="1.3"/><path d="M1.5 11.5c0-3 2-4.5 4.5-4.5s4.5 1.5 4.5 4.5z" fill="none" stroke="#0b8a84" stroke-width="1.3"/></svg></div>
    <div class="icon-btn"><svg width="12" height="12" viewBox="0 0 12 12"><rect x="1.5" y="4" width="9" height="7" rx="1.5" fill="none" stroke="#0b8a84" stroke-width="1.3"/><path d="M4 4V3a2 2 0 014 0v1" fill="none" stroke="#0b8a84" stroke-width="1.3"/></svg></div>
  </div>
</header>

<div class="abs side-card" style="left:0;border-radius:0 16px 16px 0"></div>
<div class="abs side-card" style="left:1132px;border-radius:16px 0 0 16px"></div>

<section class="abs hero">
  <div class="abs photo hero-photo" role="img" aria-label="White medical walking boot with teal sole on a wooden pedestal"></div>
  <h1 class="abs">Innovative Support<br>for Every Step</h1>
  <a class="abs btn btn-white">Shop Now</a>
  <div class="abs slides">
    <div class="bar"></div>
    <div class="cur">01</div>
    <div class="n">02</div>
    <div class="n">03</div>
    <div class="bar" style="margin-top:36px"></div>
  </div>
</section>

<h2 class="abs h2" style="top:574px">Shop Popular Category</h2>
<div class="abs cat cat-a">
  <div class="cat-blob"></div>
  <div class="cat-photo photo" role="img" aria-label="Grey and black walking boot" style="background:linear-gradient(180deg,#8d9096,#3b3d42)"></div>
  <h3>Walking Boots</h3><a class="btn btn-teal">Shop Now</a>
</div>
<div class="abs cat cat-b">
  <div class="cat-blob"></div>
  <div class="cat-photo photo" role="img" aria-label="Foot wearing a black ankle brace" style="background:linear-gradient(180deg,#c99e84,#222 35%,#1a1a1a 80%,#d3a88c)"></div>
  <h3>Ankle Brace</h3><a class="btn btn-teal">Shop Now</a>
</div>

<h2 class="abs best-title">Bestseller</h2>
<div class="abs arrow-btn" style="left:950px;top:956px;background:#fff;box-shadow:0 2px 10px rgba(0,0,0,.12)"><svg width="12" height="10" viewBox="0 0 12 10"><path d="M11 5H1m4-4L1 5l4 4" fill="none" stroke="#111" stroke-width="1.4"/></svg></div>
<div class="abs arrow-btn" style="left:991px;top:956px;background:var(--teal)"><svg width="12" height="10" viewBox="0 0 12 10"><path d="M1 5h10M7 1l4 4-4 4" fill="none" stroke="#fff" stroke-width="1.4"/></svg></div>

<div class="abs prod" style="left:163px"><div class="prod-img"><div class="ph photo" role="img" aria-label="White air walker boot" style="background:linear-gradient(180deg,#e3e6ea,#c5cad1 70%,#5fc8c8)"></div><svg class="heart" width="14" height="13" viewBox="0 0 14 13"><path d="M7 12S1 8 1 4.2A3 3 0 017 3a3 3 0 016 1.2C13 8 7 12 7 12z" fill="none" stroke="#111" stroke-width="1.2"/></svg></div><h4>Air Walker Pro</h4><div class="price">$173.99<s>$240.99</s></div><div class="go"><svg width="10" height="8" viewBox="0 0 12 10"><path d="M1 5h10M7 1l4 4-4 4" fill="none" stroke="#fff" stroke-width="1.6"/></svg></div></div>
<div class="abs prod" style="left:382px"><div class="prod-img"><div class="ph photo" role="img" aria-label="Black air walker boot" style="background:linear-gradient(180deg,#3a3c40,#1e1f22)"></div><svg class="heart" width="14" height="13" viewBox="0 0 14 13"><path d="M7 12S1 8 1 4.2A3 3 0 017 3a3 3 0 016 1.2C13 8 7 12 7 12z" fill="none" stroke="#111" stroke-width="1.2"/></svg></div><h4>Air Walker Boot</h4><div class="price">$120.99<s>$160.99</s></div><div class="go"><svg width="10" height="8" viewBox="0 0 12 10"><path d="M1 5h10M7 1l4 4-4 4" fill="none" stroke="#fff" stroke-width="1.6"/></svg></div></div>
<div class="abs prod" style="left:601px"><div class="prod-img"><div class="ph photo" role="img" aria-label="Black compression ankle brace on a foot" style="background:linear-gradient(180deg,#b7856a,#151515 25%,#151515 80%,#c99e84)"></div><svg class="heart" width="14" height="13" viewBox="0 0 14 13"><path d="M7 12S1 8 1 4.2A3 3 0 017 3a3 3 0 016 1.2C13 8 7 12 7 12z" fill="none" stroke="#111" stroke-width="1.2"/></svg></div><h4>Ankle Brace</h4><div class="price">$34.99<s>$51.99</s></div><div class="go"><svg width="10" height="8" viewBox="0 0 12 10"><path d="M1 5h10M7 1l4 4-4 4" fill="none" stroke="#fff" stroke-width="1.6"/></svg></div></div>
<div class="abs prod" style="left:820px"><div class="prod-img"><div class="ph photo" role="img" aria-label="Black adjustable ankle brace with straps" style="background:linear-gradient(180deg,#2b2b2b,#151515)"></div><svg class="heart" width="14" height="13" viewBox="0 0 14 13"><path d="M7 12S1 8 1 4.2A3 3 0 017 3a3 3 0 016 1.2C13 8 7 12 7 12z" fill="none" stroke="#111" stroke-width="1.2"/></svg></div><h4>Adjustable Ankle Brace</h4><div class="price">$35.99<s>$58.99</s></div><div class="go"><svg width="10" height="8" viewBox="0 0 12 10"><path d="M1 5h10M7 1l4 4-4 4" fill="none" stroke="#fff" stroke-width="1.6"/></svg></div></div>

<section class="abs about">
  <div class="abs about-pill1 photo" role="img" aria-label="Black ankle brace resting on a wooden shelf"></div>
  <div class="abs about-pill2 photo" role="img" aria-label="Basketball player dribbling a ball"></div>
  <h2 class="abs">About Kaltir</h2>
  <p class="abs" style="top:236px">Kaltir offers a wide range of braces and supports for orthopedic injuries, including those affecting the foot, ankle, and back. Our products are designed to provide effective relief and aid in recovery.</p>
  <p class="abs" style="top:331px">We carry leading brands and offer helpful resources like videos and expert advice to ensure you find the right brace for your needs, supporting you every step of the way.</p>
  <a class="abs btn btn-teal">Learn More</a>
</section>

<h2 class="abs h2" style="top:2008px">Why Choose Us</h2>
<div class="abs why" style="left:163px"><div class="ico"><svg width="30" height="30" viewBox="0 0 30 30" fill="none" stroke="#fff" stroke-width="1.4"><path d="M3 20h24M6 24h18M9 6v10M15 6v10M21 6v10M7 8l2-2 2 2M13 8l2-2 2 2M19 8l2-2 2 2"/></svg></div><h4>Comfort</h4><p>Soft, breathable materials for all-day comfort.</p></div>
<div class="abs why" style="left:455px"><div class="ico"><svg width="30" height="30" viewBox="0 0 30 30" fill="none" stroke="#fff" stroke-width="1.4"><circle cx="15" cy="15" r="11"/><circle cx="15" cy="15" r="6"/><path d="M15 12v3l2 2"/></svg></div><h4>Durability</h4><p>Long-lasting support with high-quality materials.</p></div>
<div class="abs why" style="left:746px"><div class="ico"><svg width="30" height="30" viewBox="0 0 30 30" fill="none" stroke="#fff" stroke-width="1.4"><circle cx="15" cy="13" r="9"/><path d="M11 13l3 3 5-6M10 21l-2 7 7-3 7 3-2-7"/></svg></div><h4>Medical-Grade Quality</h4><p>Designed to meet strict medical standards for safe recovery.</p></div>

<section class="abs reviews">
  <h2 class="abs">Our Reviews</h2>
  <div class="abs rating-sum"><span class="stars" style="font-size:13px">★★★★★</span>140 Reviews<svg width="10" height="6" viewBox="0 0 10 6"><path d="M1 1l4 4 4-4" fill="none" stroke="#111" stroke-width="1.3"/></svg></div>
  <div class="abs filter"><svg width="18" height="16" viewBox="0 0 18 16" fill="none" stroke="#111" stroke-width="1.4"><path d="M1 3h16M1 8h16M1 13h16"/><circle cx="6" cy="3" r="1.8" fill="#fff"/><circle cx="12" cy="8" r="1.8" fill="#fff"/><circle cx="7" cy="13" r="1.8" fill="#fff"/></svg></div>

  <div class="abs rev-row" style="top:133px">
    <div class="rev" style="left:-44px"><div class="stars">★★★★★</div><div class="date">3/5/2024</div><div class="who">Laura M.<span>Verified</span></div><p>Lorem Ipsum is simply dummy text of the printing and typesetting</p><div class="item"><div class="thumb"></div>Ankle Brace</div></div>
    <div class="rev" style="left:262px"><div class="stars">★★★★★</div><div class="date">3/1/2024</div><div class="who">John S.<span><svg width="11" height="11" viewBox="0 0 12 12"><circle cx="6" cy="6" r="6" fill="#0b8a84"/><path d="M3 6l2 2 4-4" fill="none" stroke="#fff" stroke-width="1.4"/></svg>Verified</span></div><p>Lorem Ipsum is simply dummy text of the printing and typesetting</p><div class="item"><div class="thumb"></div>Adjustable Ankle Brace</div></div>
    <div class="rev" style="left:568px"><div class="stars">★★★★★</div><div class="date">4/27/2024</div><div class="who">Kate L.<span><svg width="11" height="11" viewBox="0 0 12 12"><circle cx="6" cy="6" r="6" fill="#0b8a84"/><path d="M3 6l2 2 4-4" fill="none" stroke="#fff" stroke-width="1.4"/></svg>Verified</span></div><p>Lorem Ipsum is simply dummy text of the printing and typesetting</p><div class="item"><div class="thumb"></div>Air Walker Pro</div></div>
    <div class="rev" style="left:874px"><div class="stars">★★★★★</div><div class="date">2/29/2024</div><div class="who">Willem K.<span><svg width="11" height="11" viewBox="0 0 12 12"><circle cx="6" cy="6" r="6" fill="#0b8a84"/><path d="M3 6l2 2 4-4" fill="none" stroke="#fff" stroke-width="1.4"/></svg>Verified</span></div><p>Lorem Ipsum is simply dummy text of the printing and typesetting</p><div class="item"><div class="thumb"></div>Air Walker Pro</div></div>
  </div>

  <div class="abs rev-row" style="top:337px">
    <div class="rev" style="left:36px"><div class="stars">★★★★★</div><div class="date">3/9/2024</div><div class="who">Marcel<span><svg width="11" height="11" viewBox="0 0 12 12"><circle cx="6" cy="6" r="6" fill="#0b8a84"/><path d="M3 6l2 2 4-4" fill="none" stroke="#fff" stroke-width="1.4"/></svg>Verified</span></div><p>Lorem Ipsum is simply dummy text of the printing and typesetting</p><div class="item"><div class="thumb"></div>Air Walker Pro</div></div>
    <div class="rev" style="left:343px"><div class="stars">★★★★★</div><div class="date">2/21/2024</div><div class="who">Kevin<span><svg width="11" height="11" viewBox="0 0 12 12"><circle cx="6" cy="6" r="6" fill="#0b8a84"/><path d="M3 6l2 2 4-4" fill="none" stroke="#fff" stroke-width="1.4"/></svg>Verified</span></div><p>Lorem Ipsum is simply dummy text of the printing and typesetting</p><div class="item"><div class="thumb"></div>Air Walker Boot</div></div>
    <div class="rev" style="left:649px"><div class="stars">★★★★★</div><div class="date">2/17/2024</div><div class="who">Kathleen36<span><svg width="11" height="11" viewBox="0 0 12 12"><circle cx="6" cy="6" r="6" fill="#0b8a84"/><path d="M3 6l2 2 4-4" fill="none" stroke="#fff" stroke-width="1.4"/></svg>Verified</span></div><p>Lorem Ipsum is simply dummy text of the printing and typesetting</p><div class="item"><div class="thumb"></div>Ankle Brace</div></div>
    <div class="rev" style="left:955px"><div class="stars">★★★★★</div><div class="date">2/8/2024</div><div class="who">Mariska<span><svg width="11" height="11" viewBox="0 0 12 12"><circle cx="6" cy="6" r="6" fill="#0b8a84"/><path d="M3 6l2 2 4-4" fill="none" stroke="#fff" stroke-width="1.4"/></svg>Verified</span></div><p>Lorem Ipsum is simply dummy text of the printing and typesetting</p><div class="item"><div class="thumb"></div>Ankle Brace</div></div>
  </div>
</section>

<h2 class="abs h2" style="top:2925px">Our Latest Blog</h2>
<article class="abs post" style="left:163px"><div class="post-img photo" role="img" aria-label="Basketball player on an outdoor court" style="background:linear-gradient(180deg,#9fb0bd,#6f8896)"></div><div class="date"><svg width="13" height="13" viewBox="0 0 14 14" fill="none" stroke="#0b8a84" stroke-width="1.2"><rect x="1.5" y="2.5" width="11" height="10" rx="1.5"/><path d="M1.5 6h11M4.5 1v3M9.5 1v3"/></svg>OCT 23, 2024</div><div class="rule"></div><h4>Best Basketball Knee Brace</h4><p>Lorem ipsum dolor sit amet, consectetur adipiscing elit, sed do eiusmod</p><div class="more">Read More<svg width="11" height="8" viewBox="0 0 12 10"><path d="M1 5h10M7 1l4 4-4 4" fill="none" stroke="#0b8a84" stroke-width="1.4"/></svg></div></article>
<article class="abs post" style="left:457px"><div class="post-img photo" role="img" aria-label="Person in a walking boot climbing stone stairs" style="background:linear-gradient(180deg,#8c8c8c,#b9b9b9)"></div><div class="date"><svg width="13" height="13" viewBox="0 0 14 14" fill="none" stroke="#0b8a84" stroke-width="1.2"><rect x="1.5" y="2.5" width="11" height="10" rx="1.5"/><path d="M1.5 6h11M4.5 1v3M9.5 1v3"/></svg>OCT 23, 2024</div><div class="rule"></div><h4>Medical Walking Boot Guide</h4><p>Lorem ipsum dolor sit amet, consectetur adipiscing elit, sed do eiusmod</p><div class="more">Read More<svg width="11" height="8" viewBox="0 0 12 10"><path d="M1 5h10M7 1l4 4-4 4" fill="none" stroke="#0b8a84" stroke-width="1.4"/></svg></div></article>
<article class="abs post" style="left:751px"><div class="post-img photo" role="img" aria-label="Athlete holding an injured ankle" style="background:linear-gradient(180deg,#ececec,#d9d9d9)"></div><div class="date"><svg width="13" height="13" viewBox="0 0 14 14" fill="none" stroke="#0b8a84" stroke-width="1.2"><rect x="1.5" y="2.5" width="11" height="10" rx="1.5"/><path d="M1.5 6h11M4.5 1v3M9.5 1v3"/></svg>OCT 23, 2024</div><div class="rule"></div><h4>How To Put On Arvex Ankle Brace</h4><p>Lorem ipsum dolor sit amet, consectetur adipiscing elit, sed do eiusmod</p><div class="more">Read More<svg width="11" height="8" viewBox="0 0 12 10"><path d="M1 5h10M7 1l4 4-4 4" fill="none" stroke="#0b8a84" stroke-width="1.4"/></svg></div></article>

<footer class="abs footer"></footer>

<section class="abs newsletter">
  <div class="abs nl-photo photo" role="img" aria-label="Foot wearing a black ankle brace"></div>
  <h2 class="abs">Get our newsletter</h2>
  <p class="abs">Sign up for Kaltir newsletter for special offers and new products.</p>
  <div class="abs nl-form"><span>Enter Your Email</span><div class="sub">Sign Up</div></div>
</section>

<div class="abs f-logo">Kaltir</div>
<div class="abs f-col" style="left:399px"><h5>Quick Links</h5><ul><li>Home</li><li>Shop</li><li>About Us</li><li>Blog</li></ul></div>
<div class="abs f-col" style="left:609px"><h5>Customer Services</h5><ul><li>My Account</li><li>View Cart</li><li>Help</li><li>Privacy Policy</li></ul></div>
<div class="abs f-col" style="left:867px"><h5>Contact</h5>
  <div class="contact"><div class="c"><svg width="13" height="13" viewBox="0 0 14 14"><path d="M3 1l2.5 3-1.5 1.5a8 8 0 004.5 4.5L10 8.5l3 2.5-1.5 2C6 13 1 8 1 2.5z" fill="#fff"/></svg></div>+01 234 567 890</div>
  <div class="contact"><div class="c"><svg width="13" height="11" viewBox="0 0 14 11" fill="none" stroke="#fff" stroke-width="1.3"><rect x="1" y="1" width="12" height="9" rx="1"/><path d="M1 2l6 4 6-4"/></svg></div>info@kaltir.com</div>
</div>
<div class="abs follow"><svg width="12" height="11" viewBox="0 0 14 13"><path d="M7 12S1 8 1 4.2A3 3 0 017 3a3 3 0 016 1.2C13 8 7 12 7 12z" fill="none" stroke="#fff" stroke-width="1.4"/></svg>Follow on Vendly</div>
<div class="abs cards"><i></i><i></i><i></i><i></i><i></i><i></i><i></i><i></i><i></i><i></i></div>
<div class="abs copy">© Kaltir 2024</div>

</body>
</html>
```